Task Description:
I’m wanting a professionally designed 8 ½' x 11, 3 fold brochure, both sides, to print as my target audience are those people who primarily don’t have access to the internet. These items will be dropped off in the mailboxes of all households in the city.
However I do have a web site www.brightcivicpath.ca where I would like to have it as a document that can be down loaded.
This is my first foray into political office and my message needs to be clear, concise and easy to understand. The brochure should be a bit conservative yet be warm and inviting. I’ve selected two pictures that I think make sense under their respective headings, but I'm open to suggestions.I need to update my picture for the front cover.
There is the possibility of having T shirts and business cards made up, which would be in essence a simpler version of the brochure so please keep this in mind. I ask that you work with me and I will compensate you accordingly for the extras should they be required. You may want to consider making the Bright Civic Path into a logo as we own all the web extensions and have applied for copyright protection for branding purposes.
You may want to look at QM Larchfield http://www.qmlarchfield.ca/ , or the Pinecrest Bank of Canada www.pinecrestbank.com as two recognizable colour schemes here in Canada but don’t let that limit your imagination.
The content in the flier should remain intact although I am open to some minor suggestions. As you can see my talents as a graphic artist are limited hence my need for that professional make over that will give it a bit of razzle dazzle and set me out from the other candidates. So use your imagination!!
Target Market(s)
Middle age voters who may or may not have access to the internet and still prefer print
Industry/Entity Type
Conservative

```html
<!DOCTYPE html>
<html lang="en">
<head>
<meta charset="utf-8">
<title>Dean Harlow – Bright Civic Path</title>
<link href="https://fonts.googleapis.com/css2?family=Anton&family=Questrial&family=Arimo:wght@400;700&display=swap" rel="stylesheet">
<style>
  :root{
    --teal:#9dd0c3;
    --teal-deep:#6fb3a2;
    --forest:#0f5c45;
    --ink:#1a1a1a;
    --paper:#ffffff;
    --rule:#555;
  }
  *{margin:0;padding:0;box-sizing:border-box}
  html,body{width:923px;height:1200px;overflow:hidden;background:var(--paper)}
  .sheet{position:absolute;left:0;top:0;width:873px;height:1135px;transform:scale(1.05727);transform-origin:0 0;font-family:"Questrial",sans-serif;color:var(--ink)}
  .abs{position:absolute}
  .band{position:absolute;left:12px;width:849px;background:var(--teal)}
  .band-top{top:10px;height:31px}
  .band-bottom{top:1077px;height:31px}
  .rule{position:absolute;left:12px;width:849px;height:5px;background:var(--ink)}
  .panel{position:absolute;top:46px;height:1024px;border-left:1px solid var(--rule)}
  .panel-left{left:12px;width:282px}
  .panel-middle{left:294px;width:283px;background:var(--teal)}
  .panel-right{left:577px;width:284px;border-right:1px solid var(--rule)}
  .bubble-title{position:absolute;font-family:"Anton",sans-serif;font-size:19px;letter-spacing:.3px;text-shadow:1px 1px 0 #9a9a9a}
  .copy{position:absolute;font-size:12.6px;line-height:16.6px;text-align:justify}
  .center{text-align:center}
  .url{position:absolute;top:1052px;font-family:"Arimo",sans-serif;font-size:13px;width:260px;text-align:center}
  .headline{position:absolute;left:577px;width:284px;text-align:center;font-family:"Anton",sans-serif;font-size:46px;line-height:1;color:var(--ink);text-shadow:3px 3px 0 #a8a8a8}
  .connector{position:absolute;left:577px;width:284px;text-align:center;font-family:"Arimo",sans-serif}
  .region{position:absolute;left:577px;width:284px;text-align:center;font-family:"Arimo",sans-serif;font-weight:700;font-size:37px;line-height:36px}
  .name{position:absolute;left:577px;width:284px;text-align:center;font-family:"Anton",sans-serif;font-size:46px;line-height:58px;color:var(--teal);text-shadow:-1px -1px 0 var(--teal-deep),1px -1px 0 var(--teal-deep),-1px 1px 0 var(--teal-deep),2px 2px 0 #5f8f84}
  .tagline{position:absolute;left:577px;width:284px;text-align:center;font-family:"Arimo",sans-serif;font-size:23px;line-height:28px}
  .photo{position:absolute}
  .date{position:absolute;left:294px;width:283px;text-align:center;font-family:"Anton",sans-serif;font-size:29px;text-shadow:2px 2px 0 #7a8f89}
  .vote{position:absolute;left:294px;width:283px;text-align:center;font-size:29px;line-height:40px;color:#eef5f3;text-shadow:-1px -1px 0 #6a7a76,1px -1px 0 #6a7a76,-1px 1px 0 #6a7a76,1px 1px 0 #6a7a76}
  .link{font-weight:700;text-decoration:underline}
  .crop{position:absolute;background:#333}
</style>
</head>
<body>
<div class="sheet">
  <!-- printer trim marks -->
  <div class="crop" style="left:38px;top:0;width:1px;height:10px"></div>
  <div class="crop" style="left:834px;top:0;width:1px;height:10px"></div>
  <div class="crop" style="left:38px;top:1108px;width:1px;height:27px"></div>
  <div class="crop" style="left:834px;top:1108px;width:1px;height:27px"></div>
  <div class="crop" style="left:294px;top:1108px;width:1px;height:27px"></div>
  <div class="crop" style="left:577px;top:1108px;width:1px;height:27px"></div>
  <div class="crop" style="left:0;top:20px;width:12px;height:1px"></div>
  <div class="crop" style="left:861px;top:20px;width:12px;height:1px"></div>
  <div class="crop" style="left:0;top:1095px;width:12px;height:1px"></div>
  <div class="crop" style="left:861px;top:1095px;width:12px;height:1px"></div>

  <div class="band band-top"></div>
  <div class="rule" style="top:41px"></div>

  <div class="panel panel-left"></div>
  <div class="panel panel-middle"></div>
  <div class="panel panel-right"></div>

  <div class="rule" style="top:1070px"></div>
  <div class="band band-bottom"></div>

  <!-- Left panel -->
  <svg class="abs" style="left:20px;top:60px" width="270" height="140" viewBox="20 60 270 140">
    <path d="M24 64h247v98H108l-40 30 8-30H24z" fill="var(--teal)"/>
    <path d="M28 68h247v96H112l-44 30 10-30H28z" fill="#fff" stroke="var(--teal)" stroke-width="1"/>
  </svg>
  <div class="bubble-title" style="left:58px;top:106px">GETTING TO KNOW</div>

  <div class="copy center" style="left:48px;top:215px;width:190px;font-size:15.5px">Bright Civic Path</div>
  <div class="copy center" style="left:44px;top:283px;width:226px">Dean Harlow is a life long resident of Thunder Bay</div>
  <div class="copy center" style="left:44px;top:348px;width:240px">My family has served this community and area for more than 100 years.</div>
  <div class="copy" style="left:44px;top:440px;width:242px;text-align:left">Walter Henry Harlow built and managed the Northgate Elevator.<br>Frank Davidson Harlow managed the Kestrel Bay Cement facility<br>Edith Long Harlow was past president of the Chamber of Commerce.<br>Hazel Harlow is a gold medalist at the 2010 Winter Olympics.</div>
  <div class="copy" style="left:48px;top:620px;width:238px">Although I have a unique vocation through the Standards Assurance Board (SAB) and could live and work anywhere in the world I have chosen to remain and work from Thunder Bay.</div>
  <div class="copy" style="left:48px;top:760px;width:234px">On average I visit and work with more than 30 different corporations a year. I have a high pressure job as companies rely on my skills and expertise to keep them safe and operational. Solving problems, minimizing costs, maximizing production are challenges I face everyday.</div>
  <div class="url" style="left:28px">www.brightcivicpath.ca</div>

  <!-- Middle panel -->
  <svg class="abs" style="left:300px;top:60px" width="270" height="140" viewBox="300 60 270 140">
    <path d="M306 63h250v98H394l-46 30 10-30H306z" fill="var(--forest)"/>
    <path d="M310 67h250v96H398l-46 30 10-30H310z" fill="#fff" stroke="var(--forest)" stroke-width="1"/>
  </svg>
  <div class="bubble-title" style="left:329px;top:110px;font-size:17px">I'm Currently Involved With</div>

  <div class="copy" style="left:303px;top:232px;width:262px"><span class="link">Voltaris Motion Inc.</span> a newly created R&amp;D company developing electric propulsion systems for the transit industry. Our research partners consist of faculty and students from <span class="link">Shoreline Technical University.</span> So I know first hand how difficult it is to start, finance and run a new business in this city.</div>

  <div class="photo" role="img" aria-label="Photo of an electric-propulsion transit bus parked on a lot under a blue sky" style="left:305px;top:425px;width:260px;height:195px;border:1px solid #fff;background:linear-gradient(180deg,#8fb2d8 0%,#c9d9ea 42%,#d8dde0 52%,#6e7268 70%,#555a52 100%)"></div>

  <div class="copy" style="left:302px;top:646px;width:262px">As Bright Civic Path, my goal is to be mayor for two terms, maximum three. With the implementation of a long term plan we will require a fresh face to step forward to complete the process. I also feel that we should reduce the number of city councilors and use those funds to make those positions full time. Term limits should apply to all elected positions!</div>

  <div class="date" style="top:845px">ON OCT. 25th</div>
  <div class="vote" style="top:897px">Vote<br>for<br>Dean Harlow</div>
  <div class="url" style="left:305px">www.brightcivicpath.ca</div>

  <!-- Right panel -->
  <div class="headline" style="top:122px">UNLOCK</div>
  <div class="headline" style="top:184px">THE</div>
  <div class="headline" style="top:245px">POTENTIAL</div>
  <div class="connector" style="top:313px;font-size:20px">of</div>
  <div class="connector" style="top:361px;font-size:24px">The Best Small City</div>
  <div class="connector" style="top:411px;font-size:20px">in</div>
  <div class="region" style="top:454px">NORTH<br>AMERICA</div>
  <div class="name" style="top:590px">DEAN<br>HARLOW</div>

  <svg class="abs" style="left:600px;top:735px" width="230" height="220" viewBox="600 735 230 220">
    <polygon points="654,772 797,745 818,900 675,928" fill="var(--teal)"/>
    <rect x="624" y="762" width="150" height="180" fill="var(--ink)"/>
  </svg>
  <div class="photo" role="img" aria-label="Candidate head-and-shoulders portrait" style="left:633px;top:754px;width:150px;height:172px;border:1px solid #333;border-top-right-radius:20px;background:#fff;padding:3px">
    <div style="width:100%;height:100%;border-top-right-radius:17px;background:linear-gradient(180deg,#e4e4e4 0%,#bdbdbd 55%,#3a3a3a 100%)"></div>
  </div>

  <div class="tagline" style="top:951px">YOUR<br>NEXT<br>MAYOR</div>
  <div class="url" style="left:590px">www.brightcivicpath.ca</div>
</div>
</body>
</html>
```